Business card design needed

We require business cards for our young and innovative construction team.

Our business is Brask Constructions and we have used Lime, Navy and white with our colours so far.

We would like business cards that show our passion for perfection and detail, communication and management.

Looking forward to seeing the deigns!!

Contact Information for Business Card

Dan Pellow
Brask Constructions Pty Ltd
PO Box 782 Quarrow Flats NSW 2795
Mobile: 0471 392 608
Email: dpellow@braskconstructions.com.au
Web: www.braskconstructions.com.au

```html
<!DOCTYPE html>
<html lang="en">
<head>
<meta charset="utf-8">
<title>Brask Constructions – Business Card</title>
<link href="https://fonts.googleapis.com/css2?family=Open+Sans:wght@400;600;700&display=swap" rel="stylesheet">
<style>
  :root {
    --navy: #2c3a66;
    --navy-deep: #24315a;
    --lime: #8dc63f;
    --white: #ffffff;
    --ink-grey: #5d6068;
    --page: #ecebe8;
  }
  * { box-sizing: border-box; margin: 0; padding: 0; }
  html, body {
    width: 1200px; height: 1024px; overflow: hidden;
    background: var(--page);
    font-family: "Open Sans", Arial, sans-serif;
  }
  .card {
    position: absolute; left: 250px;
    width: 700px; height: 400px;
    border-radius: 4px; overflow: hidden;
    box-shadow: 0 6px 20px rgba(0,0,0,0.12);
  }
  .card-front { top: 70px; background: var(--white); }
  .card-back {
    top: 554px;
    background: radial-gradient(ellipse at 50% 45%, #34457a 0%, var(--navy) 55%, var(--navy-deep) 100%);
  }

  .brand { display: flex; align-items: center; gap: 12px; }
  .brand-square { width: 22px; height: 22px; background: var(--lime); }
  .brand-name { font-weight: 600; letter-spacing: 0.5px; }

  .card-front .brand { position: absolute; left: 60px; top: 70px; }
  .card-front .brand-name { color: var(--navy); font-size: 34px; }

  .contact { position: absolute; left: 60px; top: 160px; color: var(--ink-grey); font-size: 15px; line-height: 24px; }
  .contact-name { color: var(--navy); font-weight: 700; font-size: 26px; line-height: 34px; margin-bottom: 4px; }
  .contact-line { display: flex; align-items: center; gap: 8px; }
  .contact-line svg { width: 14px; height: 14px; fill: var(--lime); flex: none; }

  .front-band { position: absolute; left: 0; bottom: 0; width: 700px; height: 70px; }
  .front-web {
    position: absolute; right: 26px; bottom: 20px;
    color: var(--white); font-size: 14px; letter-spacing: 0.3px;
  }

  .card-back .brand { position: absolute; left: 0; right: 0; top: 160px; justify-content: center; }
  .card-back .brand-name { color: var(--white); font-size: 42px; }
  .card-back .brand-square { width: 28px; height: 28px; }
  .back-web {
    position: absolute; left: 0; right: 0; top: 240px; text-align: center;
    color: var(--white); font-size: 16px; letter-spacing: 0.4px;
  }
</style>
</head>
<body>
  <section class="card card-front">
    <div class="brand">
      <span class="brand-square"></span>
      <span class="brand-name">Brask Constructions</span>
    </div>
    <div class="contact">
      <p class="contact-name">Dan Pellow</p>
      <p>Brask Constructions Pty Ltd</p>
      <p>PO Box 782 Quarrow Flats NSW 2795</p>
      <p class="contact-line">
        <svg viewBox="0 0 24 24" aria-hidden="true"><path d="M6.6 10.8a15.1 15.1 0 0 0 6.6 6.6l2.2-2.2a1 1 0 0 1 1-.25 11.4 11.4 0 0 0 3.6.57 1 1 0 0 1 1 1V20a1 1 0 0 1-1 1A17 17 0 0 1 3 4a1 1 0 0 1 1-1h3.5a1 1 0 0 1 1 1c0 1.25.2 2.45.57 3.6a1 1 0 0 1-.25 1z"/></svg>
        0471 392 608
      </p>
      <p class="contact-line">
        <svg viewBox="0 0 24 24" aria-hidden="true"><path d="M2 5h20v14H2z M3 6l9 7 9-7" /></svg>
        dpellow@braskconstructions.com.au
      </p>
    </div>
    <svg class="front-band" viewBox="0 0 700 70" aria-hidden="true">
      <polygon points="0,46 436,46 484,2 700,2 700,70 0,70" fill="var(--lime)"/>
      <polygon points="0,62 446,62 494,12 700,12 700,70 0,70" fill="var(--navy)"/>
    </svg>
    <p class="front-web">www.braskconstructions.com.au</p>
  </section>

  <section class="card card-back">
    <div class="brand">
      <span class="brand-square"></span>
      <span class="brand-name">Brask Constructions</span>
    </div>
    <p class="back-web">www.braskconstructions.com.au</p>
  </section>
</body>
</html>
```